Corvanta512 Business Card Redesign

I want to create a design for brand new business cards, I need something exceptional for clear plastic business card design. Please do not submit without it being on a clear design. Photos of the various logo versions attached.

```html
<!DOCTYPE html>
<html lang="en">
<head>
<meta charset="utf-8">
<title>Corvanta512 Business Card</title>
<link href="https://fonts.googleapis.com/css2?family=Arimo:wght@400;700&display=swap" rel="stylesheet">
<style>
  :root {
    --page: #bdb3a5;
    --frost-top: rgba(255, 255, 255, 0.42);
    --frost-bottom: rgba(255, 255, 255, 0.22);
    --edge: rgba(255, 255, 255, 0.75);
    --navy: #1d2538;
    --navy-text: #1f2a44;
    --gold: #b68a3c;
    --gold-dark: #8a6422;
    --body-text: #2a2a2e;
    --divider: #6f6c6a;
    --band-text: #c9b9a3;
    --mark-tint: rgba(200, 215, 235, 0.55);
  }
  html, body {
    margin: 0;
    padding: 0;
    width: 1200px;
    height: 969px;
    overflow: hidden;
    background: var(--page);
    font-family: "Arimo", Arial, sans-serif;
  }
  .card {
    position: absolute;
    left: 100px;
    top: 198px;
    width: 1000px;
    height: 572px;
    background:
      linear-gradient(115deg, rgba(255,255,255,0.18) 0%, rgba(255,255,255,0) 35%, rgba(255,255,255,0.14) 60%, rgba(255,255,255,0) 100%),
      linear-gradient(180deg, var(--frost-top), var(--frost-bottom));
    border: 1px solid var(--edge);
    box-sizing: border-box;
    box-shadow: 0 4px 18px rgba(0,0,0,0.12), inset 0 0 0 1px rgba(255,255,255,0.25);
    overflow: hidden;
  }
  .brand-mark {
    position: absolute;
    left: 240px;
    top: 128px;
    width: 160px;
    height: 160px;
    border-radius: 50%;
    background: radial-gradient(circle at 50% 45%, var(--mark-tint), rgba(200,215,235,0.15));
  }
  .brand {
    position: absolute;
    left: 0;
    width: 640px;
    top: 302px;
    text-align: center;
    color: var(--gold);
    font-size: 50px;
    font-weight: 700;
    letter-spacing: 1px;
  }
  .divider {
    position: absolute;
    left: 507px;
    top: 110px;
    width: 2px;
    height: 260px;
    background: var(--divider);
    opacity: 0.55;
  }
  .details {
    position: absolute;
    left: 540px;
    top: 108px;
    color: var(--body-text);
  }
  .person-name {
    margin: 0;
    font-size: 38px;
    font-weight: 700;
    color: var(--navy-text);
    letter-spacing: 0.5px;
    line-height: 42px;
  }
  .person-title {
    margin: 2px 0 0;
    font-size: 21px;
    color: var(--gold-dark);
  }
  .address {
    margin: 28px 0 0;
    font-size: 22px;
    line-height: 30px;
    font-style: normal;
  }
  .contacts {
    list-style: none;
    margin: 16px 0 0;
    padding: 0;
    font-size: 22px;
  }
  .contacts li {
    display: flex;
    align-items: center;
    height: 30px;
  }
  .contacts svg {
    width: 20px;
    height: 20px;
    margin-right: 16px;
    fill: var(--navy-text);
  }
  .band {
    position: absolute;
    left: 0;
    top: 470px;
    width: 1000px;
    height: 51px;
  }
  .band-navy {
    position: absolute;
    left: 0;
    top: 0;
    width: 782px;
    height: 51px;
    background: linear-gradient(90deg, var(--navy), #2a3147);
  }
  .website {
    position: absolute;
    left: 165px;
    top: 14px;
    font-size: 21px;
    letter-spacing: 4px;
    color: var(--band-text);
  }
  .band-mark {
    position: absolute;
    left: 797px;
    top: 9px;
    width: 33px;
    height: 33px;
    border-radius: 50%;
    background: var(--navy);
  }
  .band-gold {
    position: absolute;
    left: 846px;
    top: 0;
    width: 154px;
    height: 51px;
    background: linear-gradient(90deg, var(--gold-dark), var(--gold));
  }
</style>
</head>
<body>
  <div class="card">
    <div class="brand-mark"></div>
    <div class="brand">Corvanta512</div>
    <div class="divider"></div>
    <div class="details">
      <h1 class="person-name">DANIEL HARROW</h1>
      <p class="person-title">President</p>
      <address class="address">4216 Alder Crest Way<br>Halden, Canada 52817</address>
      <ul class="contacts">
        <li>
          <svg viewBox="0 0 24 24" aria-hidden="true"><path d="M6.6 10.8a15.1 15.1 0 0 0 6.6 6.6l2.2-2.2c.3-.3.7-.4 1-.2 1.1.4 2.3.6 3.6.6.6 0 1 .4 1 1V20c0 .6-.4 1-1 1C10.6 21 3 13.4 3 4c0-.6.4-1 1-1h3.5c.6 0 1 .4 1 1 0 1.3.2 2.5.6 3.6.1.3 0 .7-.2 1z"/></svg>
          555-218-4470
        </li>
        <li>
          <svg viewBox="0 0 24 24" aria-hidden="true"><path d="M7 1h10a2 2 0 0 1 2 2v18a2 2 0 0 1-2 2H7a2 2 0 0 1-2-2V3a2 2 0 0 1 2-2zm0 3v15h10V4z"/></svg>
          555-309-6128
        </li>
        <li>
          <svg viewBox="0 0 24 24" aria-hidden="true"><path d="M2 6h20v13H2zm2 2v.5l8 5 8-5V8l-8 5z"/></svg>
          info@corvanta512.com
        </li>
      </ul>
    </div>
    <div class="band">
      <div class="band-navy"><span class="website">www.corvanta512.com</span></div>
      <div class="band-mark"></div>
      <div class="band-gold"></div>
    </div>
  </div>
</body>
</html>
```